Voltrane Corporate Info Poster For Promoting Brand Identity

We need to create a "poster" that is currently set on an 11" x 17" size that will explain who we are, what we do, and who are clients are. We need it themed to develop our brand and we need to be able to edit the wording, as well as add logos when needed.

I am including an example of one that was done for another company I worked at, as well as the content we need.

There is also a brochure we have that I am including as which has a map with our locations on it. IF the design can include a map of our locations underneath the logos, that would be great, providing there is enough room.

Logos of our customers are labeled either logo or screenshot.

I have also included our corporate logo

They "poster" we had made prior is listed as "example 1"

Also, I have uploaded the content and categories the new design should have. Content wording is only suggestions. If you can create better wording that is more direct yet promoting, feel free to change wording if needed.

Target Market(s)

All customers in the manufacturing industry

Requirements
Must have
• Corporate logo, focus on branding,
Nice to have
• Looking for someone to be imaginative here, want this energetic and self promoting.
Should not have
• Open to imagination

```html
<!DOCTYPE html>
<html lang="en">
<head>
<meta charset="utf-8">
<title>Voltrane Corporate Info Poster</title>
<link href="https://fonts.googleapis.com/css2?family=Montserrat:wght@400;600;700&family=Open+Sans:wght@400;600;700&display=swap" rel="stylesheet">
<style>
:root{
  --navy:#0d1a33;
  --blue:#1f6aa5;
  --red:#b8222a;
  --red-bright:#d7262c;
  --ink:#2a2a2a;
  --grey-band:#efefef;
  --white:#ffffff;
}
*{margin:0;padding:0;box-sizing:border-box}
html,body{width:856px;height:1200px;overflow:hidden;background:#fff}
.poster{position:relative;width:856px;height:1200px;font-family:"Open Sans",sans-serif;color:var(--ink);overflow:hidden}
.hero{position:absolute;left:0;top:0;width:856px;height:420px}
.hero svg{position:absolute;left:0;top:0}
.brand{position:absolute;left:26px;top:24px;display:flex;align-items:center;gap:8px}
.brand-mark{width:20px;height:20px;border-radius:50%;background:var(--red-bright)}
.brand-name{font-family:"Montserrat",sans-serif;font-weight:600;font-size:34px;color:var(--red-bright);line-height:1}
.machine{position:absolute;border-radius:6px;background:linear-gradient(160deg,#e8eaec,#9ca3aa 60%,#d9dcdf)}
.tagline{position:absolute;top:384px;left:0;width:856px;text-align:center;font-size:12.5px;line-height:1.4;color:var(--red-bright)}
.tab{position:absolute;left:0;height:22px;width:210px;border-radius:0 11px 11px 0;font-family:"Montserrat",sans-serif;font-size:12.5px;color:#fff;padding:3px 0 0 38px;letter-spacing:.3px}
.tab.blue{background:var(--blue)}
.tab.red{background:var(--red)}
.copy{position:absolute;left:38px;width:786px;font-size:8.4px;line-height:1.4}
.copy p{margin-bottom:5px}
.copy .bullet::before{content:"•";color:var(--red-bright);margin-right:4px}
.service-band{position:absolute;left:0;top:597px;width:856px;height:201px;background:var(--blue)}
.service-band .copy{color:#fff;top:20px;font-size:8.6px}
.clients-band{position:absolute;left:0;top:904px;width:856px;height:148px;background:var(--grey-band)}
.clients{position:absolute;left:38px;top:56px;width:786px;display:grid;grid-template-columns:repeat(9,1fr);row-gap:22px;align-items:center;text-align:center}
.client{font-family:"Open Sans",sans-serif;font-weight:700;font-size:11px;line-height:1.1}
.footer{position:absolute;left:0;top:1052px;width:856px;height:148px;background:var(--red)}
.map{position:absolute;left:38px;top:10px;width:286px;height:124px;border-radius:4px;background:radial-gradient(ellipse at 45% 45%,#d64a4f,#b8222a 70%)}
.offices{position:absolute;left:344px;top:12px;width:500px;display:grid;grid-template-columns:1fr 1fr 1.25fr 1.1fr;column-gap:8px;row-gap:24px;color:#fff;font-size:5.9px;line-height:1.35}
.offices b{display:block;font-weight:700}
</style>
</head>
<body>
<div class="poster">
  <section class="hero">
    <svg width="856" height="420" viewBox="0 0 856 420" aria-hidden="true">
      <defs>
        <linearGradient id="heroGrad" x1="1" y1="0" x2="0" y2="1">
          <stop offset="0" stop-color="#07101f"/>
          <stop offset=".55" stop-color="#17335e"/>
          <stop offset="1" stop-color="#275a94"/>
        </linearGradient>
      </defs>
      <path d="M0,335 C150,230 350,90 545,0 L856,0 L856,400 C800,345 720,318 620,312 C450,300 150,318 0,372 Z" fill="url(#heroGrad)"/>
      <path d="M0,372 C150,318 450,300 620,312 C720,318 800,345 856,400 L856,412 C800,370 720,346 620,340 C450,330 150,350 0,408 Z" fill="#b8222a"/>
    </svg>
    <div class="brand"><span class="brand-mark"></span><span class="brand-name">Voltrane</span></div>
    <div class="machine" style="left:49px;top:70px;width:167px;height:211px" role="img" aria-label="Photo of a horizontal ribbon mixer"></div>
    <div class="machine" style="left:265px;top:65px;width:135px;height:234px" role="img" aria-label="Photo of a vacuum mixer reactor"></div>
    <div class="machine" style="left:485px;top:70px;width:113px;height:225px" role="img" aria-label="Photo of a conical screw mixer on a frame"></div>
    <div class="machine" style="left:669px;top:80px;width:145px;height:206px" role="img" aria-label="Photo of a stainless steel process vessel"></div>
  </section>

  <p class="tagline">Voltrane is an Israel based engineering &amp; manufacturing company that provides innovative,<br>performance driven mixing solutions across all industries since 1954</p>

  <div class="tab blue" style="top:422px">What We Make</div>
  <div class="copy" style="top:452px">
    <p>Voltrane leads the industry in innovative, performance driven, Value Added Engineering mixing solutions of all types for all industries. With over 28 types of mixers, we lead the industry in mixing solutions when it comes to mixing powders, liquids, or pastes. The largest selection of mixers available of ANY brand in the industry.<br>Our three main core focuses are:</p>
    <p class="bullet">Stand Alone, Single Machine Offerings: Our stand alone, single machine offerings set standard specifications with Value Added Engineering, allowing for high performance, top tier quality, &amp; semi-custom configurations to be ordered with ease at a cost effective price</p>
    <p class="bullet">Our OEM division has built some of the best brands in the industry, with no minimum orders, no contracts, &amp; incredible quality, it is no wonder others rely on us to build their brand.</p>
    <p class="bullet">Our Custom Engineered Products division has engineered &amp; manufactured for global industry leaders, as well as the needs of entrepreneurs globally, allowing for history to be made as well as start ups to succeed. From single item solutions to complete lines, Voltrane can provide complete, system integrated, turn key projects.</p>
  </div>

  <section class="service-band">
    <div class="copy">
      <p>Voltrane leads the industry in innovation, but innovation also needs to be maintained &amp; backed. As such, Voltrane's philosophy of "Sustainability through superior engineering" has allowed Voltrane to accelerate in markets others fail. Our standardization of parts combined with our streamlined approach to service has enabled us to minimize downtime &amp; maximize customer satisfaction on a global level, something most other brands fail at.<br>Our Service &amp; Support Team have three main categories and is developed to provide service &amp; support:</p>
      <p>• <b>FACILITY SPONSORED SERVICE:</b> For larger facilities that have in-house engineering teams Voltrane has an in-house training program that is hands on, virtual, &amp; web based supported. Custom spare parts packages can be designed to minimize down time &amp; maximize efficiency of maintenance crews</p>
      <p>• <b>VOLTRANE SPONSORED SERVICE &amp; SUPPORT:</b> Voltrane aligns with local service partners in areas where service is needed and facilities are not large enough to have their own teams. Voltrane offers the same support &amp; training to these teams &amp; spare parts packages will be sent into regions where installations are commissioned. If an area does not currently have support, Voltrane will, during the lead time of building a machine, meet &amp; negotiate with respected regional service teams, negotiate a contract, train, &amp; supply parts, allowing customers to be confident in our service &amp; support.</p>
      <p>• <b>FACILITY SPONSORED, EXTERNAL SERVICE:</b> For companies that currently have a working relationship with a service provider, Voltrane will meet &amp; negotiate service terms, train, &amp; support with spare parts packages, allowing companies to maintain comfort levels of service while maximizing the ability of Voltrane to service the equipment if needed in confidence.</p>
    </div>
  </section>
  <div class="tab red" style="top:588px;width:200px">Service &amp; Support</div>

  <div class="tab blue" style="top:809px">Warranty</div>
  <div class="copy" style="top:838px">
    <p>Voltrane's approach to warranty is unsurpassed in the industry, ensuring a quick ROI for customers, while providing warranty coverage well after ROI is achieved, ensuring profits stay where they belong, in the customers pockets. Our Global Warranty Coverage focuses on minimized down time, maximized customer service, &amp; quick response in a time of need. Globally, Voltrane has a cost of warranty that is below 2% per year. This is a result of our stellar quality &amp; standards Voltrane sets in our production standards.</p>
  </div>

  <section class="clients-band">
    <div class="copy" style="top:22px"><p>From the entrepreneurs of today, to the leading brands of yesteryear &amp; today, as well as the start ups of tomorrow, Voltrane serves all industries with our mixing solutions.</p></div>
    <div class="clients">
      <span class="client" style="color:#c8202a">Printforge</span>
      <span class="client" style="color:#d7262c">Tackwell</span>
      <span class="client" style="color:#3b7a3a">Fieldora</span>
      <span class="client" style="color:#1b3f8f">Kenrow Tape</span>
      <span class="client" style="color:#c8202a">Saffra</span>
      <span class="client" style="color:#1f4fa0">Ambercrest</span>
      <span class="client" style="color:#d7262c">Aquaterra</span>
      <span class="client" style="color:#c8202a">Goodmix Foods</span>
      <span class="client" style="color:#1b3f8f">Scentara</span>
      <span class="client" style="color:#d7262c">Brixon</span>
      <span class="client" style="color:#2c5e9e">Riverline</span>
      <span class="client" style="color:#8a6d3b">Lotus Pantry</span>
      <span class="client" style="color:#c8202a">Mesa Dulce</span>
      <span class="client" style="color:#444">Quikform</span>
      <span class="client" style="color:#c8202a">Cleanroll</span>
      <span class="client" style="color:#d7262c">Candor Sweets</span>
      <span class="client" style="color:#1f6aa5">Springvale</span>
      <span class="client" style="color:#c8202a">Orchard Lane</span>
    </div>
  </section>
  <div class="tab blue" style="top:893px">Who We Serve</div>

  <footer class="footer">
    <div class="map" role="img" aria-label="Dotted world map marking Voltrane office locations"></div>
    <div class="offices">
      <div><b>Voltrane in China</b>Shanghai, 200000, China<br>Contact: Mr. Leo Chen<br>Tel: +86 100 555 0101<br>Email: leo.c@voltrane.example</div>
      <div><b>Voltrane in Israel</b>Adi 10000, Israel<br>Contact: Mr. Dan Levin<br>Tel: +972-50-555-0102<br>Email: dlevin@voltrane.example</div>
      <div><b>South America office</b>Buenos Aires, Argentina<br>Contact: Mr. Mateo Rojas<br>Tel: +54-9-11-5550103<br>Email: mateo.rojas@voltrane.example</div>
      <div><b>UK office</b>Scotland, UK<br>Contact: Mr. Owen Hale<br>Tel: +44 (0) 7700 900104<br>Email: owen.hale@voltrane.example</div>
      <div><b>Voltrane North America</b>Chicago, Illinois,<br>60000, USA<br>Contact: Mr. Mark Ellis<br>Tel: +1 630-555-0105<br>Email: mark.ellis@voltrane.example</div>
      <div><br><b>South Africa office</b>South Africa<br>Contact: Mr. Peter Nolan<br>Email: za@voltrane.example</div>
      <div><br><b>Russia office</b>Contact: Mr. Ivan Sorokin<br>Tel: +7 900 555 0106<br>Email: ru@voltrane.example</div>
      <div><br><b>Ukraine office</b>Contact: Mr. Oleg Marchenko<br>Tel: +38 067 555 0107<br>Email: ua@voltrane.example</div>
    </div>
  </footer>
</div>
</body>
</html>
```